Flyer for Custom Home Builder!

my company is Harlow Ridge Homes, I am looking for a flyer that we can send via email to a customer, or print and hand out. I am thinking four pages so we could print this and fold it., possibly creating a folder. The name of the company is Harlow Ridge Homes our website is here www.harlowridgehomes-example.com. Some text you can use "Crafting luxury homes isn't just a job, it's our passion.
With meticulous attention to detail and an unwavering commitment to using the finest materials, Harlow Ridge Homes consistently delivers exceptional results that stand as a testament to our commitment to quality."

"Trust is the cornerstone of our foundation.
With a proven track record of delivering on our promises for over 16 years, we prioritize transparent communication and integrity throughout every step of the home-building journey".

you may need to obtain the photos here
https://files.example-share.net/f/k27pw4m8zrt03xq61bnv/h?key=48vn2c9q1x7mb5t0ekd3h&dl=0

Target Market(s)

We build homes for every wealthy clients, therefore the photos are extremely important

Industry/Entity Type

Construction.

Requirements
Must have
• clear larger photos

```html
<!DOCTYPE html>
<html lang="en">
<head>
<meta charset="utf-8">
<title>Harlow Ridge Homes – Folded Brochure</title>
<link rel="stylesheet" href="https://fonts.googleapis.com/css2?family=Playfair+Display:wght@400;500&display=swap">
<style>
  :root{
    --bg:#e4e4e4;
    --paper:#f7f7f7;
    --ink:#3f3f42;
    --ink-soft:#6b6b6e;
    --rule:#8d8d90;
    --kitchen-top:#eeeeec;
    --kitchen-mid:#d9dadb;
    --kitchen-navy:#33435a;
    --kitchen-floor:#6f6a65;
    --dusk-sky:#a86fb8;
    --dusk-pink:#e49ab8;
    --stone:#d8d2c6;
    --lawn:#4f6b3a;
    --pool:#56b6cf;
  }
  *{box-sizing:border-box;margin:0;padding:0}
  html,body{width:1200px;height:3270px;overflow:hidden}
  body{background:var(--bg);font-family:"Playfair Display",Georgia,serif;color:var(--ink);position:relative}

  .scene{position:absolute;left:0;width:1200px}
  .scene--cover{top:0;height:1040px}
  .scene--outer{top:1040px;height:1070px}
  .scene--inner{top:2110px;height:1160px}

  .spread{position:absolute;display:flex;box-shadow:0 18px 40px rgba(0,0,0,.18)}
  .page{position:relative;width:500px;height:725px;background:var(--paper);overflow:hidden}
  .page + .page{border-left:1px solid #dcdcdc}

  .scene--cover .spread{left:313px;top:105px;transform:scale(1.15);transform-origin:top left}
  .scene--outer .spread{left:100px;top:172px}
  .scene--inner .spread{left:90px;top:205px;transform:scale(1.02);transform-origin:top left}

  /* cover */
  .brand{font-family:"Playfair Display",Georgia,serif;font-weight:500;color:var(--ink);letter-spacing:.04em;line-height:1}
  .cover .brand{position:absolute;left:34px;top:58px;font-size:28px}
  .cover .tagline{position:absolute;left:34px;top:142px;font-size:25px;line-height:1.3;font-weight:400}
  .cover .rule{position:absolute;left:34px;right:0;top:222px;height:1px;background:var(--rule)}
  .photo{position:absolute}
  .photo--kitchen{left:0;right:0;top:228px;bottom:0;
    background:linear-gradient(180deg,var(--kitchen-top) 0%,#f4f4f3 28%,var(--kitchen-mid) 52%,var(--kitchen-navy) 64%,#5a6474 72%,var(--kitchen-floor) 80%,#595450 100%)}
  .cover .web{position:absolute;left:34px;bottom:38px;color:#fff;font-size:13px;letter-spacing:.32em}

  /* back */
  .photo--dusk{left:36px;top:56px;width:426px;height:322px;
    background:linear-gradient(180deg,#7f5da8 0%,var(--dusk-sky) 18%,var(--dusk-pink) 30%,var(--stone) 48%,#9a948c 68%,var(--lawn) 84%,#3d5230 100%)}
  .back{text-align:center}
  .back .brand{position:absolute;left:0;right:0;top:470px;font-size:28px}
  .back .phone{position:absolute;left:0;right:0;top:583px;font-size:25px}
  .back .email{position:absolute;left:0;right:0;top:628px;font-size:13px}
  .back .address{position:absolute;left:0;right:0;top:658px;font-size:12px;line-height:1.35}

  /* inner */
  .copy{font-size:16px;line-height:1.3;color:var(--ink)}
  .inner-left .copy{position:absolute;left:40px;right:30px;top:62px}
  .inner-left .rule{position:absolute;left:40px;right:0;top:190px;height:1px;background:var(--rule)}
  .photo--facade{left:40px;right:30px;top:210px;bottom:42px;
    background:linear-gradient(180deg,#cfd0d8 0%,#e2d3d9 22%,#5a5f68 40%,#e3e0da 62%,#b9b6b0 78%,#2f2f2c 100%)}
  .photo--terrace{left:30px;right:40px;top:48px;height:262px;
    background:linear-gradient(180deg,#9b7fb8 0%,#e3a3bd 24%,#51555c 46%,#d7d2c9 70%,#3b3b3d 100%)}
  .photo--pool{left:30px;right:40px;top:318px;height:258px;
    background:linear-gradient(180deg,#eef1f2 0%,#c9cfd2 30%,#6e6154 48%,#d9d6cf 62%,var(--pool) 80%,#3b98b2 100%)}
  .inner-right .rule{position:absolute;left:30px;right:40px;top:592px;height:1px;background:var(--rule)}
  .inner-right .copy{position:absolute;left:30px;right:34px;top:604px;font-size:15px}
</style>
</head>
<body>

<section class="scene scene--cover" aria-label="Front cover">
  <div class="spread">
    <article class="page cover">
      <div class="brand">Harlow Ridge Homes</div>
      <p class="tagline">Crafting luxury homes<br>isn't just a job, it's our passion.</p>
      <div class="rule"></div>
      <div class="photo photo--kitchen" role="img" aria-label="Bright white luxury kitchen with gold pendant lights, navy island and upholstered bar stools"></div>
      <div class="web">www.harlowridgehomes-example.com</div>
    </article>
  </div>
</section>

<section class="scene scene--outer" aria-label="Outer spread">
  <div class="spread">
    <article class="page back">
      <div class="photo photo--dusk" role="img" aria-label="Modern stone custom home at dusk with purple sky and curved paver driveway"></div>
      <div class="brand">Harlow Ridge Homes</div>
      <p class="phone">+1 555-014-2786</p>
      <p class="email">info@harlowridgehomes-example.com</p>
      <p class="address">480 Cedar Vale Rd, Austin,<br>TX, United States, Texas</p>
    </article>
    <article class="page cover">
      <div class="brand">Harlow Ridge Homes</div>
      <p class="tagline">Crafting luxury homes<br>isn't just a job, it's our passion.</p>
      <div class="rule"></div>
      <div class="photo photo--kitchen" role="img" aria-label="Bright white luxury kitchen with gold pendant lights, navy island and upholstered bar stools"></div>
      <div class="web">www.harlowridgehomes-example.com</div>
    </article>
  </div>
</section>

<section class="scene scene--inner" aria-label="Inner spread">
  <div class="spread">
    <article class="page inner-left">
      <p class="copy">With meticulous attention to detail and an unwavering commitment to using the finest materials, Harlow Ridge Homes consistently delivers exceptional results that stand as a testament to our commitment to quality.</p>
      <div class="rule"></div>
      <div class="photo photo--facade" role="img" aria-label="Two-storey modern home facade with dark cladding, white stone and large windows at twilight"></div>
    </article>
    <article class="page inner-right">
      <div class="photo photo--terrace" role="img" aria-label="Outdoor terrace lounge of a stone home under a pink evening sky"></div>
      <div class="photo photo--pool" role="img" aria-label="Backyard swimming pool and spa beside a modern covered patio"></div>
      <div class="rule"></div>
      <p class="copy">Trust is the cornerstone of our foundation. With a proven track record of delivering on our promises for over 16 years, we prioritize transparent communication and integrity throughout every step of the home-building journey.</p>
    </article>
  </div>
</section>

</body>
</html>
```